Tour agency for FIT and groups need a business card design

We need a business card design for a tour agency company that is based in Perth called" BRISK NO", we aim to provide customise, unique and seamless travel arrangement for FIT and groups. We serve both high profile businessperson, government authorities, business partners, executives and investors. The name card should be more professional looking.
Updates

Project Deadline Extended Reason: Have some changes that needed to make, director will be back to office on Monday, sorry for the inconvenience cause. Added Saturday, May 6, 2017

Target Market(s)

High profile businessperson, government authorities, business partners, executives and investors.

Industry/Entity Type

Tourism

Contact Information for Business Card

Brisk NO
Level 1, 214 Marlowe Avenue, Dunreath NO, 6120
www.briskno.com.au

Font styles to use
Serif

Colors

Designer to choose colors to be used in the design.

Requirements
Must have
• My project must have a company logo
Nice to have
• a more professional and solid yet friendly name card design. We may want to include chinese name in the name card as well. Edge of the card can be filled with gold and we think that transparent name cards are interesting.

```html
<!DOCTYPE html>
<html lang="en">
<head>
<meta charset="utf-8">
<title>Brisk NO – Business Card</title>
<link rel="stylesheet" href="https://fonts.googleapis.com/css2?family=Roboto:wght@400;500&display=swap">
<style>
  :root {
    --page-bg: #e9e7e4;
    --card-front: #ffffff;
    --card-back: #1b1b1b;
    --brand-blue: #2ba3dd;
    --ink: #4a4a4a;
    --ink-soft: #555555;
    --shadow: rgba(0, 0, 0, 0.28);
  }
  * { margin: 0; padding: 0; box-sizing: border-box; }
  html, body {
    width: 1200px;
    height: 1200px;
    overflow: hidden;
    background: var(--page-bg);
    font-family: "Roboto", Arial, sans-serif;
  }
  .canvas { position: relative; width: 1200px; height: 1200px; }
  .card {
    position: absolute;
    left: 215px;
    width: 772px;
    height: 438px;
    border-radius: 18px;
    box-shadow: 0 6px 18px var(--shadow);
  }
  .card--front { top: 151px; background: var(--card-front); }
  .card--back  { top: 634px; background: var(--card-back); }

  .brand-mark {
    position: absolute;
    display: flex;
    align-items: center;
    gap: 12px;
    color: var(--brand-blue);
    font-weight: 500;
    white-space: nowrap;
  }
  .brand-mark__dot {
    border-radius: 50%;
    background: var(--brand-blue);
    flex: none;
  }
  .card--front .brand-mark { left: 80px; top: 186px; font-size: 46px; }
  .card--front .brand-mark__dot { width: 18px; height: 18px; }
  .card--back .brand-mark {
    left: 50%; top: 50%;
    transform: translate(-50%, -50%);
    font-size: 78px; gap: 18px;
  }
  .card--back .brand-mark__dot { width: 28px; height: 28px; }

  .divider {
    position: absolute;
    left: 387px; top: 100px;
    width: 2px; height: 240px;
    background: var(--brand-blue);
  }
  .details { position: absolute; left: 423px; top: 88px; color: var(--ink); }
  .details__name { font-size: 31px; font-weight: 500; line-height: 1.1; color: var(--ink); }
  .details__role { font-size: 20px; color: var(--brand-blue); margin-top: 4px; }
  .details__company { font-size: 21px; font-weight: 500; margin-top: 20px; }
  .details__address { font-size: 18.5px; line-height: 1.45; color: var(--ink-soft); margin-top: 4px; font-style: normal; }
  .contact-list { list-style: none; margin-top: 14px; }
  .contact-list li {
    display: flex; align-items: center; gap: 8px;
    font-size: 18.5px; line-height: 1.5; color: var(--ink-soft);
  }
  .contact-list svg { width: 17px; height: 17px; flex: none; }
</style>
</head>
<body>
<main class="canvas">
  <section class="card card--front" aria-label="Business card front">
    <div class="brand-mark"><span class="brand-mark__dot"></span>Brisk NO</div>
    <div class="divider"></div>
    <div class="details">
      <h1 class="details__name">Marcus Hale</h1>
      <p class="details__role">President &amp; CEO</p>
      <p class="details__company">Brisk NO</p>
      <address class="details__address">Level 1, 214 Marlowe Avenue<br>Dunreath NO, 6120</address>
      <ul class="contact-list">
        <li>
          <svg viewBox="0 0 24 24" fill="none" stroke="var(--brand-blue)" stroke-width="1.6" stroke-linejoin="round"><path d="M5 3h4l2 5-2.5 1.5a11 11 0 0 0 6 6L16 13l5 2v4a2 2 0 0 1-2 2A16 16 0 0 1 3 5a2 2 0 0 1 2-2z"/></svg>
          000-000-0000
        </li>
        <li>
          <svg viewBox="0 0 24 24" fill="none" stroke="var(--brand-blue)" stroke-width="1.6"><rect x="3" y="5" width="18" height="14"/><path d="M3 5l9 8 9-8"/></svg>
          m.hale@briskno.com.au
        </li>
        <li>
          <svg viewBox="0 0 24 24" fill="none" stroke="var(--brand-blue)" stroke-width="1.6"><circle cx="12" cy="12" r="9"/><ellipse cx="12" cy="12" rx="4" ry="9"/><path d="M3 12h18M5 7h14M5 17h14"/></svg>
          www.briskno.com.au
        </li>
      </ul>
    </div>
  </section>

  <section class="card card--back" aria-label="Business card back">
    <div class="brand-mark"><span class="brand-mark__dot"></span>Brisk NO</div>
  </section>
</main>
</body>
</html>
```